Dallas Texas Special Event Center Flyer

Need a new brochure (small 8.5 x 11 tri-fold) for an event center in Dallas, Texas area. It is located on a golf course and is ideal for weddings, quinceaneras, retirement parties, etc. Is best known for weddings. There is no logo for the event center. I have attached the prior brochure, which is not professional. We do not have any site photos.

Target Market(s)

people seeking special event space in dallas, texas area. Brides, meeting planners, etc.

Industry/Entity Type

Golf Course

Font styles to use
Script
Other font styles liked:
• combine serif and some use of script ok

Requirements
Must have
• lots of photos - see attached

```html
<!DOCTYPE html>
<html lang="en">
<head>
<meta charset="utf-8">
<title>Event Center at Willowbend – Tri-fold Brochure</title>
<link href="https://fonts.googleapis.com/css2?family=Great+Vibes&family=Tinos:wght@400;700&display=swap" rel="stylesheet">
<style>
  :root{
    --teal:#0f86a6;
    --teal-deep:#0a6f8c;
    --teal-light:#1fa2c4;
    --yellow:#e6d823;
    --ring:#2aa9de;
    --white:#ffffff;
    --ink:#2e2e2e;
    --stage:#d9dcdf;
    --script:"Great Vibes", cursive;
    --serif:"Tinos", "Times New Roman", serif;
  }
  *{box-sizing:border-box;margin:0;padding:0}
  html,body{width:1200px;height:899px;overflow:hidden;background:var(--stage)}
  .brochure{position:absolute;left:36px;top:14px;width:1128px;height:872px;display:flex;box-shadow:0 6px 24px rgba(0,0,0,.25)}
  .panel{position:relative;width:376px;height:872px;overflow:hidden;background:var(--white)}
  .panel svg.bg{position:absolute;inset:0;width:376px;height:872px}
  .url-bar{position:absolute;left:30px;right:30px;bottom:30px;height:44px;border-radius:14px;background:var(--yellow);
    display:flex;align-items:center;justify-content:center;font-family:var(--serif);font-size:15px;color:var(--ink)}
  /* inside panel */
  .venue-copy{position:absolute;left:24px;right:24px;top:478px;font-family:var(--serif);font-size:11px;line-height:1.36;color:var(--white);text-align:justify}
  .venue-copy p{margin-bottom:8px}
  /* contact panel */
  .contact-title{position:absolute;left:22px;top:22px;font-family:var(--script);font-size:30px;line-height:1.05;color:var(--ink)}
  .contact-list{position:absolute;left:22px;top:112px;list-style:none;font-family:var(--serif);font-size:12.5px;line-height:1.35;color:var(--ink)}
  .contact-list li{display:flex;gap:10px;margin-bottom:8px}
  .contact-list svg{flex:none;width:10px;height:10px;margin-top:3px}
  .location-copy{position:absolute;left:30px;right:30px;top:672px;font-family:var(--serif);font-size:14.5px;line-height:1.32;color:var(--white);text-align:justify;text-align-last:center}
  /* cover */
  .brand{position:absolute;left:0;right:0;top:36px;text-align:center;font-family:var(--serif);font-weight:700;font-size:19px;color:#3a3a3a}
  .brand-dot{display:block;margin:0 auto 10px;width:46px;height:46px;border-radius:50%;background:#9a9a9a}
  .cover-title{position:absolute;left:0;right:0;top:664px;text-align:center;font-family:var(--script);color:var(--white)}
  .cover-title .line1{display:block;font-size:44px;line-height:1}
  .cover-title .line2{display:block;font-size:32px;line-height:1.1}
  .cover-title .tagline{display:block;font-size:25px;color:var(--yellow);line-height:1.2}
</style>
</head>
<body>
<main class="brochure">

  <section class="panel panel-venue">
    <svg class="bg" viewBox="0 0 376 872" aria-hidden="true">
      <defs><linearGradient id="tealA" x1="0" y1="0" x2="0" y2="1"><stop offset="0" stop-color="#1592b3"/><stop offset="1" stop-color="#0b7594"/></linearGradient>
      <linearGradient id="toastPhoto" x1="0" y1="0" x2="1" y2="1"><stop offset="0" stop-color="#c9a37e"/><stop offset=".5" stop-color="#e8d6bc"/><stop offset="1" stop-color="#7d6a58"/></linearGradient></defs>
      <rect width="376" height="872" fill="url(#tealA)"/>
      <path d="M0 462 Q190 398 376 392 V412 Q190 420 0 484 Z" fill="var(--white)"/>
      <path d="M0 440 Q190 376 376 368 V396 Q190 402 0 466 Z" fill="var(--yellow)"/>
      <path d="M0 0 H376 V372 Q190 380 0 444 Z" fill="url(#toastPhoto)" role="img" aria-label="Photo of wedding guests and bride raising champagne glasses in a toast"/>
    </svg>
    <div class="venue-copy">
      <p>The Event Center at Willowbend offers a 12,000 square foot facility which boasts a Grand Ballroom and two Banquet rooms.</p>
      <p>The grand ballroom will accommodate 809 guests for a wedding ceremony and reception, quinceanera, retirement party or any occasion that demands a large-scale, elegant setting.</p>
      <p>The bridal suite at the top of the winding staircase allows the Bride and her bridesmaids to prepare for the big day out of sight of arriving guests, allowing a dramatic grand entrance.</p>
      <p>Banquet room 1 will accommodate 103 guests for a mid-size, private event such as a birthday or retirement party or company holiday party while Banquet room 2 will accommodate 35 guests for a small intimate event such as a bridal shower, bridesmaid's luncheon or corporate training. The rooms can be used separately or together.</p>
      <p>The event center has a full commercial kitchen onsite to cater any event from formal dining to buffet-style. The menu can be customized to your specifications and will be prepared by our expert chef and his team.</p>
      <p>The Event Center at Willowbend is the perfect location for your wedding, conference, seminar, party, reunion or graduation.</p>
    </div>
    <div class="url-bar">www.eventcenteratwillowbend.com</div>
  </section>

  <section class="panel panel-contact">
    <svg class="bg" viewBox="0 0 376 872" aria-hidden="true">
      <defs><linearGradient id="tealB" x1="0" y1="0" x2="0" y2="1"><stop offset="0" stop-color="#1592b3"/><stop offset="1" stop-color="#0b7594"/></linearGradient>
      <linearGradient id="flowerPhoto" x1="0" y1="0" x2="1" y2="1"><stop offset="0" stop-color="#f3eee9"/><stop offset=".55" stop-color="#eac9cf"/><stop offset="1" stop-color="#cfd8cf"/></linearGradient></defs>
      <path d="M0 470 C140 440 240 500 376 650 V872 H0 Z" fill="url(#tealB)"/>
      <path d="M296 0 C236 210 262 470 376 664 V618 C294 460 278 220 336 0 Z" fill="var(--yellow)"/>
      <path d="M336 0 C278 220 294 460 376 618 V0 Z" fill="url(#tealB)"/>
      <circle cx="190" cy="520" r="130" fill="var(--white)"/>
      <circle cx="190" cy="520" r="124" fill="none" stroke="var(--ring)" stroke-width="7"/>
      <circle cx="190" cy="520" r="114" fill="url(#flowerPhoto)" role="img" aria-label="Photo of a vase of pink and white roses on a reception table"/>
    </svg>
    <h2 class="contact-title">Contact us for more information<br>or Visit us at:</h2>
    <ul class="contact-list">
      <li><svg viewBox="0 0 10 10"><circle cx="5" cy="5" r="4" fill="none" stroke="#d8c21c" stroke-width="1.5"/></svg>www.eventcenteratwillowbend.com</li>
      <li><svg viewBox="0 0 10 10"><rect x="1" y="2" width="8" height="6" fill="#d8c21c"/><path d="M1 2 L5 5.5 L9 2" fill="none" stroke="#fff" stroke-width=".8"/></svg><span>Laura Bennett<br>laura@eventcenteratwillowbend.com</span></li>
      <li><svg viewBox="0 0 10 10"><path d="M2 1 L4 1 L5 3 L4 4 Q5 6 6 6 L7 5 L9 6 L9 8 Q5 9 1 3 Z" fill="#d8c21c"/></svg>214-555-0142</li>
      <li><svg viewBox="0 0 10 10"><rect x="3" y="1" width="4" height="8" rx="1" fill="#d8c21c"/></svg>972-555-0187</li>
      <li><svg viewBox="0 0 10 10"><path d="M5 1 L9 5 H8 V9 H2 V5 H1 Z" fill="#d8c21c"/></svg><span>Event Center at Willowbend<br>1480 E Highway 90<br>Maple Ridge, TX 75000</span></li>
    </ul>
    <p class="location-copy">The Event Center at Willowbend is located on Willowbend Golf Course, an 18-hole, 215-acre championship golf course in Maple Ridge, Texas and is surrounded by rolling hills, seven beautiful lakes, creeks, pecan orchards and many varieties of wildlife.</p>
    <div class="url-bar">www.eventcenteratwillowbend.com</div>
  </section>

  <section class="panel panel-cover">
    <svg class="bg" viewBox="0 0 376 872" aria-hidden="true">
      <defs><linearGradient id="tealC" x1="0" y1="0" x2="0" y2="1"><stop offset="0" stop-color="#1a9abd"/><stop offset="1" stop-color="#0a6f8c"/></linearGradient>
      <linearGradient id="couplePhoto" x1="0" y1="0" x2="1" y2="1"><stop offset="0" stop-color="#7f9a5a"/><stop offset=".5" stop-color="#e9e4da"/><stop offset="1" stop-color="#5f7a42"/></linearGradient></defs>
      <rect width="376" height="872" fill="url(#tealC)"/>
      <path d="M30 0 H376 V180 H60 C40 120 30 60 30 0 Z" fill="var(--white)"/>
      <path d="M376 150 V660 C250 668 110 630 44 520 C0 420 10 250 80 160 C180 148 300 146 376 150 Z" fill="var(--yellow)"/>
      <path d="M376 160 V642 C255 650 120 612 58 510 C20 420 28 260 92 170 C185 158 300 156 376 160 Z" fill="url(#couplePhoto)" role="img" aria-label="Photo of a bride and groom walking outdoors as guests toss petals"/>
    </svg>
    <div class="brand"><span class="brand-dot"></span>eventcenteratwillowbend.com</div>
    <h1 class="cover-title"><span class="line1">Host Your Event</span><span class="line2">at the</span><span class="tagline">Dallas Area's Premiere Event Venue</span></h1>
    <div class="url-bar">www.eventcenteratwillowbend.com</div>
  </section>

</main>
</body>
</html>
```